We are in search of a new business card design for our business. We have a Mexican Grocery Store called Tortilla Grove Market, we would like to see that some have mexican design, but we are open to any type of designs.

Phone: to be announced
Fax: to be announced

Address is:
2415 Calloway Blvd
Dundalk, MD 21222

```html
<!DOCTYPE html>
<html lang="en">
<head>
<meta charset="utf-8">
<title>Tortilla Grove Market – Business Card</title>
<link rel="stylesheet" href="https://fonts.googleapis.com/css2?family=Rubik:wght@500;600;700&display=swap">
<style>
  :root {
    --backdrop: #e6e1d7;
    --card: #f1d98e;
    --card-edge: #e7cc7c;
    --chevron: #a7a274;
    --ink: #35363a;
    --accent-red: #a8191c;
    --icon-green: #2f8a3f;
    --divider: #3b3b3b;
  }
  * { margin: 0; padding: 0; box-sizing: border-box; }
  html, body {
    width: 1200px;
    height: 900px;
    overflow: hidden;
    background: var(--backdrop);
    font-family: "Rubik", Arial, sans-serif;
  }
  .business-card {
    position: absolute;
    left: 145px;
    top: 185px;
    width: 910px;
    height: 530px;
    background: linear-gradient(180deg, var(--card) 0%, var(--card-edge) 100%);
    box-shadow: 0 6px 18px rgba(0,0,0,0.18);
  }
  .pattern-band {
    position: absolute;
    top: 0;
    width: 57px;
    height: 100%;
    background: linear-gradient(90deg, var(--chevron), #c9c08a, var(--chevron));
  }
  .pattern-band.left { left: 0; }
  .pattern-band.right { right: 0; }

  .brand {
    position: absolute;
    left: 110px;
    top: 215px;
    width: 340px;
    display: flex;
    align-items: center;
    gap: 16px;
  }
  .brand-dot {
    flex: none;
    width: 44px;
    height: 44px;
    border-radius: 50%;
    background: var(--accent-red);
  }
  .brand-name {
    font-weight: 700;
    font-size: 36px;
    line-height: 1.1;
    color: var(--accent-red);
  }

  .divider {
    position: absolute;
    left: 479px;
    top: 177px;
    width: 2px;
    height: 184px;
    background: var(--divider);
  }

  .contact {
    position: absolute;
    left: 524px;
    top: 160px;
    color: var(--ink);
  }
  .person-name {
    font-weight: 700;
    font-size: 34px;
    letter-spacing: 0.5px;
    line-height: 1;
  }
  .person-role {
    margin-top: 6px;
    font-weight: 500;
    font-size: 21px;
    color: var(--accent-red);
  }
  .address {
    margin-top: 14px;
    font-weight: 500;
    font-size: 21px;
    line-height: 31px;
  }
  .numbers { margin-top: 13px; list-style: none; }
  .numbers li {
    display: flex;
    align-items: center;
    gap: 12px;
    font-weight: 600;
    font-size: 23px;
    line-height: 31px;
  }
  .numbers svg { width: 22px; height: 22px; fill: var(--icon-green); }
</style>
</head>
<body>
  <main class="business-card">
    <div class="pattern-band left" role="img" aria-label="Vertical zigzag chevron border pattern"></div>
    <div class="pattern-band right" role="img" aria-label="Vertical zigzag chevron border pattern"></div>

    <div class="brand">
      <span class="brand-dot"></span>
      <span class="brand-name">Tortilla Grove Market</span>
    </div>

    <div class="divider"></div>

    <section class="contact">
      <h1 class="person-name">MARCO REYES</h1>
      <p class="person-role">Owner</p>
      <p class="address">2415 Calloway Blvd<br>Dundalk, MD 21222</p>
      <ul class="numbers">
        <li>
          <svg viewBox="0 0 24 24" aria-label="Phone"><path d="M6.6 10.8a15.1 15.1 0 0 0 6.6 6.6l2.2-2.2c.3-.3.7-.4 1-.2 1.1.4 2.3.6 3.6.6.6 0 1 .4 1 1V20c0 .6-.4 1-1 1A17 17 0 0 1 3 4c0-.6.4-1 1-1h3.5c.6 0 1 .4 1 1 0 1.3.2 2.5.6 3.6.1.3 0 .7-.2 1z"/></svg>
          045-281-906
        </li>
        <li>
          <svg viewBox="0 0 24 24" aria-label="Fax"><path d="M7 3h10v4H7zM4 8h16a2 2 0 0 1 2 2v6h-4v5H6v-5H2v-6a2 2 0 0 1 2-2zm4 7v4h8v-4zm10-4a1 1 0 1 0 0 2 1 1 0 0 0 0-2z"/></svg>
          234-590-718
        </li>
      </ul>
    </section>
  </main>
</body>
</html>
```